Business Card, A4 Letter Head and DL Envelope for Brandolux

We are looking for a design for our Business Card, A4 Letter Head and DL Envelope.

Brandolux is a distributor of promotional products. We specialize in a range of branded promotional products, these include pens, polo shirts, key rings, drink bottles, uniforms and bags to name a few. We are experts in marketing and assist companies in choosing the right promotional product for their needs. We will predominately be an online business where customers visit our website and browse our range of promotional products and branding options.

Our colours are black, red, white and grey.

Files must be supplied in eps, pdf and ai format.

Please display the following information:
Dorian Pell
Account Manager
Suite xxx, 214 Harwick Lane Melbourne, Victoria 3000
Phone +61 3 5550 1842
Mobile +61 455 501 736
sales@brandolux.example
www.brandolux.example

```html
<!DOCTYPE html>
<html lang="en">
<head>
<meta charset="utf-8">
<title>Brandolux Business Card</title>
<link rel="stylesheet" href="https://fonts.googleapis.com/css2?family=Source+Sans+3:wght@400;600;700&display=swap">
<style>
  :root {
    --stage: #000000;
    --card: #ffffff;
    --ink: #1e1e1e;
    --brand-red: #e8254c;
    --brand-grey: #5f6064;
    --mark-grey: #c9cacc;
  }
  * { margin: 0; padding: 0; box-sizing: border-box; }
  html, body {
    width: 1200px;
    height: 459px;
    overflow: hidden;
    background: var(--stage);
  }
  body {
    position: relative;
    font-family: "Source Sans 3", sans-serif;
    color: var(--ink);
  }
  .card {
    position: absolute;
    top: 84px;
    width: 485px;
    height: 296px;
    background: var(--card);
  }
  .card--front { left: 98px; }
  .card--back { left: 616px; }

  .brand-mark {
    position: absolute;
    left: 181px;
    top: 75px;
    width: 122px;
    height: 122px;
  }
  .brand-name {
    position: absolute;
    left: 0;
    width: 100%;
    top: 203px;
    text-align: center;
    font-weight: 700;
    font-size: 42px;
    letter-spacing: 1px;
    color: var(--brand-grey);
    text-transform: uppercase;
  }

  .person {
    position: absolute;
    left: 54px;
    top: 49px;
  }
  .person__name {
    font-weight: 700;
    font-size: 21px;
    line-height: 24px;
    color: var(--brand-red);
  }
  .person__role {
    font-size: 17px;
    line-height: 22px;
  }

  .contact {
    position: absolute;
    left: 240px;
    top: 91px;
    font-size: 15px;
    line-height: 18px;
  }
  .contact__row { display: flex; }
  .contact__label {
    width: 70px;
    font-weight: 700;
    color: var(--brand-red);
  }
  .contact__address { margin-top: 15px; }
  .contact__online { margin-top: 16px; }
  .contact__web {
    font-weight: 700;
    color: var(--brand-red);
  }
</style>
</head>
<body>
  <section class="card card--front">
    <svg class="brand-mark" viewBox="0 0 122 122" aria-hidden="true">
      <circle cx="61" cy="61" r="60" fill="var(--mark-grey)"/>
    </svg>
    <div class="brand-name">Brandolux</div>
  </section>

  <section class="card card--back">
    <div class="person">
      <div class="person__name">Dorian Pell</div>
      <div class="person__role">Account Manager</div>
    </div>
    <div class="contact">
      <div class="contact__row"><span class="contact__label">Phone</span><span>+61 3 5550 1842</span></div>
      <div class="contact__row"><span class="contact__label">Mobile</span><span>+61 455 501 736</span></div>
      <address class="contact__address" style="font-style:normal">
        Suite xxx, 214 Harwick<br>
        Lane Melbourne, Victoria,<br>
        3000
      </address>
      <div class="contact__online">
        <div class="contact__email">sales@brandolux.example</div>
        <div class="contact__web">www.brandolux.example</div>
      </div>
    </div>
  </section>
</body>
</html>
```